Scientific project description

Here is a project description related to cellular mechanics, showing above the forces acting on cells in the tissues of our body. The forces on single cells are there to depict how forces are acting on cells (pressure squeezes the cell, shear flow is pushing the upward parts of the cell, tension pulls one part of the cell, strain is stretching the whole cell; the single cell images are to be found also on the last page). Intense red/purple are used to indicate that the forces are stressful (the colors to be used do not need to be exactly like these colors). The picture in the middle is a view of cells (same picture on next page if that needs to be modified). At the left, a description of what happens when everything is going well, i.e. the body stays healthy. At the right, if you dysfunction you get disease. Green nuances were used to indicate health, brownish, perhaps not so pleasant nuances were used to indicate disease. Below are the steps of the project.

On the whole, we're rather happy with the concept description as such, but it should look a little bit nicer. To many color nuances give a "noisy" impression, fonts could be nicer, layout more crisp, and the text on the steps should be more readable. We would also like to have two versions of the same picture, one with black background, one with white.

Target Market(s)

Scientists that are evaluating our project

Requirements
Must have
• Easy to grasp the idea, easy to read and understand the underlying idea.
Nice to have
• Would be good to have the Concept title ("Vorlint Concept and Envisioned Project Progression) on top of the figure as indicated in the second brief picture submitted.

```html
<!DOCTYPE html>
<html lang="en">
<head>
<meta charset="utf-8">
<title>Vorlint – Concept and Envisioned Project Progression</title>
<link rel="stylesheet" href="https://fonts.googleapis.com/css2?family=Montserrat:wght@400;500;600;700&family=Oswald:wght@500&family=Roboto:wght@400;500;700&display=swap">
<style>
  :root{
    --bg-center:#ffffff;
    --bg-edge:#e4e5e7;
    --ink:#111111;
    --tab:#2b2b2b;
    --white:#ffffff;
    --health:#4cba5a;
    --health-deep:#1e6b34;
    --health-dark:#0f5a2a;
    --frail:#f2b08a;
    --frail-deep:#7a3a18;
    --disease-band:#8a4a24;
    --micro-dark:#0c2410;
    --micro-green:#2f7a35;
    --hex-force:#e0623a;
    --hex-response:#c0283a;
    --hex-disease:#7a1030;
    --hex-machinery:#7b2d8e;
    --hex-targets:#8a5a3c;
    --hex-prevention:#0f5a2a;
    --hex-therapies:#4cba5a;
  }
  *{margin:0;padding:0;box-sizing:border-box}
  html,body{width:1200px;height:1000px;overflow:hidden}
  body{background:radial-gradient(ellipse at 50% 55%,var(--bg-center) 0%,var(--bg-edge) 75%);font-family:'Roboto',Arial,sans-serif;color:var(--ink)}
  .canvas{position:relative;width:1200px;height:1000px}
  .diagram{position:absolute;inset:0}
  .title{position:absolute;top:104px;left:0;width:1200px;text-align:center;font-family:'Montserrat',Arial,sans-serif;font-weight:600;font-size:50px;letter-spacing:1px;line-height:1;color:var(--ink)}
  .subtitle{position:absolute;top:157px;left:0;width:1200px;text-align:center;font-family:'Montserrat',Arial,sans-serif;font-weight:400;font-size:24px;line-height:1.2;color:var(--ink)}
  .force-tab{position:absolute;width:138px;text-align:center;font-family:'Montserrat',Arial,sans-serif;font-weight:600;font-size:14px;letter-spacing:3px;color:var(--white)}
  .state-label{position:absolute;font-size:13px;line-height:1.15;text-align:center;color:var(--white)}
  .state-label.dark{color:#3a2010}
  .core-label{position:absolute;left:487px;top:566px;width:226px;text-align:center;font-family:'Oswald',Arial,sans-serif;font-weight:500;font-size:25px;letter-spacing:.5px;color:var(--white)}
  .step{position:absolute;width:100px;text-align:center;font-family:'Roboto',Arial,sans-serif;font-weight:500;font-size:10.5px;line-height:1.3;text-transform:uppercase;color:var(--ink)}
</style>
</head>
<body>
<main class="canvas">
  <svg class="diagram" width="1200" height="1000" viewBox="0 0 1200 1000" xmlns="http://www.w3.org/2000/svg">
    <defs>
      <linearGradient id="card-pressure" x1="0" y1="0" x2="0" y2="1"><stop offset="0" stop-color="#e0683a"/><stop offset="1" stop-color="#c81e30"/></linearGradient>
      <linearGradient id="card-shear" x1="0" y1="0" x2="0" y2="1"><stop offset="0" stop-color="#c01e2e"/><stop offset="1" stop-color="#9e2840"/></linearGradient>
      <linearGradient id="card-tension" x1="0" y1="0" x2="0" y2="1"><stop offset="0" stop-color="#c0183a"/><stop offset="1" stop-color="#4a0820"/></linearGradient>
      <linearGradient id="card-strain" x1="0" y1="0" x2="0" y2="1"><stop offset="0" stop-color="#9a2a9a"/><stop offset="1" stop-color="#66288a"/></linearGradient>
      <radialGradient id="micro" cx="0.5" cy="0.5" r="0.6"><stop offset="0" stop-color="var(--micro-green)"/><stop offset="1" stop-color="var(--micro-dark)"/></radialGradient>
      <marker id="arrowhead" viewBox="0 0 10 10" refX="9" refY="5" markerWidth="7" markerHeight="7" orient="auto-start-reverse"><path d="M0 0 L10 5 L0 10 z" fill="var(--ink)"/></marker>
    </defs>

    <!-- force cards -->
    <g class="force-card">
      <path d="M303 265 q0-9 9-9 h120 q9 0 9 9 v20 h-138z" fill="var(--tab)"/>
      <polygon points="365,285 377,285 371,294" fill="var(--tab)"/>
      <rect x="303" y="287" width="138" height="111" rx="6" fill="url(#card-pressure)" role="img" aria-label="Cell squeezed by pressure from above"/>
      <circle cx="368" cy="400" r="18" fill="url(#micro)" stroke="var(--white)" stroke-width="3" role="img" aria-label="Micrograph of a cell under pressure"/>
    </g>
    <g class="force-card">
      <path d="M456 251 q0-9 9-9 h118 q9 0 9 9 v20 h-136z" fill="var(--tab)"/>
      <polygon points="518,271 530,271 524,280" fill="var(--tab)"/>
      <rect x="456" y="273" width="136" height="110" rx="6" fill="url(#card-shear)" role="img" aria-label="Cell pushed sideways by shear flow"/>
      <circle cx="523" cy="382" r="18" fill="url(#micro)" stroke="var(--white)" stroke-width="3" role="img" aria-label="Micrograph of a cell under shear"/>
    </g>
    <g class="force-card">
      <path d="M607 251 q0-9 9-9 h120 q9 0 9 9 v20 h-138z" fill="var(--tab)"/>
      <polygon points="670,271 682,271 676,280" fill="var(--tab)"/>
      <rect x="607" y="273" width="138" height="110" rx="6" fill="url(#card-tension)" role="img" aria-label="Cell pulled upward by tension"/>
      <circle cx="677" cy="382" r="18" fill="url(#micro)" stroke="var(--white)" stroke-width="3" role="img" aria-label="Micrograph of a cell under tension"/>
    </g>
    <g class="force-card">
      <path d="M760 265 q0-9 9-9 h119 q9 0 9 9 v20 h-137z" fill="var(--tab)"/>
      <polygon points="822,285 834,285 828,294" fill="var(--tab)"/>
      <rect x="760" y="287" width="137" height="111" rx="6" fill="url(#card-strain)" role="img" aria-label="Cell stretched on both sides by strain"/>
      <circle cx="829" cy="400" r="18" fill="url(#micro)" stroke="var(--white)" stroke-width="3" role="img" aria-label="Micrograph of a cell under strain"/>
    </g>

    <!-- connectors into the core -->
    <g class="connectors" fill="none" stroke="var(--ink)" stroke-width="2">
      <polyline points="368,418 368,425 548,425 548,462" marker-end="url(#arrowhead)"/>
      <polyline points="523,400 523,407 580,407 580,462" marker-end="url(#arrowhead)"/>
      <polyline points="677,400 677,407 617,407 617,462" marker-end="url(#arrowhead)"/>
      <polyline points="829,418 829,425 648,425 648,462" marker-end="url(#arrowhead)"/>
      <polyline points="375,601 375,652 400,652" marker-end="url(#arrowhead)"/>
      <polyline points="823,601 823,654 807,654" marker-end="url(#arrowhead)"/>
    </g>

    <!-- state labels -->
    <g class="states">
      <rect x="383" y="495" width="90" height="28" fill="var(--health)"/>
      <polygon points="478,495 520,495 505,523 463,523" fill="var(--health-deep)"/>
      <polygon points="680,495 722,495 737,523 695,523" fill="var(--frail-deep)"/>
      <rect x="725" y="495" width="97" height="28" fill="var(--frail)"/>

      <polygon points="288,563 460,563 472,582 460,601 288,601" fill="var(--health-deep)"/>
      <polyline points="486,567 474,582 486,597" fill="none" stroke="var(--ink)" stroke-width="5"/>
      <polygon points="725,563 911,563 911,601 725,601 737,582" fill="var(--disease-band)"/>
      <polyline points="714,567 726,582 714,597" fill="none" stroke="var(--ink)" stroke-width="5"/>

      <rect x="402" y="639" width="72" height="27" fill="var(--health)"/>
      <polygon points="478,639 520,639 505,666 463,666" fill="var(--health-deep)"/>
      <polygon points="680,639 722,639 737,666 695,666" fill="var(--frail-deep)"/>
      <rect x="725" y="639" width="72" height="27" fill="var(--frail)"/>
    </g>

    <!-- core hexagon -->
    <polygon class="core" points="487,582 540,486 660,486 713,582 660,677 540,677" fill="url(#micro)" stroke="var(--health)" stroke-width="2" role="img" aria-label="Fluorescence micrograph of cells with green cytoskeleton"/>

    <!-- project steps -->
    <g class="steps" fill="none" stroke-width="7">
      <polygon points="294,763 321,716 375,716 402,763 375,810 321,810" stroke="var(--hex-force)"/>
      <polygon points="379,813 406,766 460,766 487,813 460,860 406,860" stroke="var(--hex-response)"/>
      <polygon points="465,763 492,716 546,716 573,763 546,810 492,810" stroke="var(--hex-disease)"/>
      <polygon points="551,813 578,766 632,766 659,813 632,860 578,860" stroke="var(--hex-machinery)"/>
      <polygon points="636,763 663,716 717,716 744,763 717,810 663,810" stroke="var(--hex-targets)"/>
      <polygon points="721,813 748,766 802,766 829,813 802,860 748,860" stroke="var(--hex-prevention)"/>
      <polygon points="805,763 832,716 886,716 913,763 886,810 832,810" stroke="var(--hex-therapies)"/>
    </g>
  </svg>

  <h1 class="title">VORLINT</h1>
  <p class="subtitle">Concept and Envisioned Project Progression</p>

  <span class="force-tab" style="left:303px;top:263px">PRESSURE</span>
  <span class="force-tab" style="left:455px;top:249px">SHEAR</span>
  <span class="force-tab" style="left:607px;top:249px">TENSION</span>
  <span class="force-tab" style="left:760px;top:263px">STRAIN</span>

  <span class="state-label" style="left:383px;top:503px;width:90px">Cell fitness</span>
  <span class="state-label dark" style="left:725px;top:503px;width:97px">Cell Frailty</span>
  <span class="state-label" style="left:292px;top:567px;width:168px">Functional cellular<br>machineries</span>
  <span class="state-label" style="left:740px;top:567px;width:171px">Disfunctional cellular<br>machineries</span>
  <span class="state-label" style="left:402px;top:646px;width:80px">Health</span>
  <span class="state-label dark" style="left:725px;top:646px;width:62px">Disease</span>

  <span class="core-label">MECHANOSTASIS</span>

  <span class="step" style="left:298px;top:749px">Mechanical<br>force models</span>
  <span class="step" style="left:383px;top:792px">Cell, tissue<br>and organ<br>responses</span>
  <span class="step" style="left:469px;top:749px">Disease<br>models</span>
  <span class="step" style="left:555px;top:799px">Cellular<br>machineries</span>
  <span class="step" style="left:640px;top:749px">Critical<br>targets</span>
  <span class="step" style="left:725px;top:806px">Prevention</span>
  <span class="step" style="left:809px;top:756px">Therapies</span>
</main>
</body>
</html>
```